Cozy Nest to Grand Estate - House

This will be converted to vinyl signage for the windows in front of my building dimensions are approximately 9 feet long by six feet high
I would like a creative design showing three homes in One
the homes should progress from
a typical first home
to a mid-level upgrade home,
then a fabulous dream home
I like the concept in the picture with the homes growing in size but i don't like the plane little homes

I would like this designed in photoshop

Target Market(s)

24-50 age renage

Industry/Entity Type

Real Estate Agent

Logo Text

Cozy Nest to Grand Estate

Font styles to use
Sans Serif

Requirements
Must have
• color scheme to match the included logo
• I am searching for homes that are the same color
• grey, white or maroon,
• or perhaps the same build material (stone or brick) and still show the same progression from small 1st home to final luxury home

```html
<!DOCTYPE html>
<html lang="en">
<head>
<meta charset="utf-8">
<title>Cozy Nest to Grand Estate – Window Sign</title>
<link href="https://fonts.googleapis.com/css2?family=Montserrat:wght@500;600&display=swap" rel="stylesheet">
<style>
  :root {
    --stage: #2a2a2c;
    --panel-light: #ffffff;
    --panel-mid: #d9d9db;
    --maroon: #c2486a;
    --maroon-dark: #8e2f4a;
    --slate: #474d55;
    --ink-light: #ffffff;
    --house-light: #f1f1f1;
    --house-mid: #9aa0a8;
  }
  html, body {
    margin: 0;
    width: 1200px;
    height: 1000px;
    overflow: hidden;
    background: var(--stage);
  }
  .sign {
    position: absolute;
    left: 60px;
    top: 139px;
    width: 1080px;
    height: 722px;
    box-shadow: 0 10px 30px rgba(0,0,0,.55);
  }
  .sign svg { display: block; width: 100%; height: 100%; }
  .contact-text, .brand-name {
    font-family: "Montserrat", sans-serif;
  }
  .contact-text { font-size: 17px; font-weight: 500; fill: var(--ink-light); }
  .brand-name { font-size: 14px; font-weight: 600; fill: var(--maroon-dark); }
</style>
</head>
<body>
  <div class="sign">
    <svg viewBox="0 0 560 374" xmlns="http://www.w3.org/2000/svg">
      <defs>
        <linearGradient id="panelGradient" x1="0" y1="0" x2="1" y2="0">
          <stop offset="0" stop-color="var(--panel-mid)"/>
          <stop offset="0.45" stop-color="var(--panel-light)"/>
          <stop offset="1" stop-color="var(--panel-mid)"/>
        </linearGradient>
        <linearGradient id="houseGradient" x1="0" y1="0" x2="0" y2="1">
          <stop offset="0" stop-color="var(--house-mid)"/>
          <stop offset="0.45" stop-color="var(--house-light)"/>
          <stop offset="1" stop-color="#cfd3cf"/>
        </linearGradient>
      </defs>

      <rect class="panel" width="560" height="374" fill="url(#panelGradient)"/>

      <polyline class="growth-band-shadow" points="0,130 130,70 138,104 305,26 312,66 400,44 407,78 560,8"
        fill="none" stroke="var(--slate)" stroke-width="12" stroke-linejoin="miter" opacity=".35"/>
      <polyline class="growth-band" points="0,126 130,66 138,100 305,22 312,62 400,40 407,74 560,4"
        fill="none" stroke="var(--maroon)" stroke-width="13" stroke-linejoin="miter"/>

      <rect class="house house-starter" x="28" y="152" width="62" height="68" rx="3"
        fill="url(#houseGradient)" role="img" aria-label="Photo of a small white starter cottage"/>
      <rect class="house house-upgrade" x="140" y="137" width="140" height="80" rx="3"
        fill="url(#houseGradient)" role="img" aria-label="Photo of a mid-size grey colonial home"/>
      <rect class="house house-dream" x="320" y="97" width="235" height="112" rx="3"
        fill="url(#houseGradient)" role="img" aria-label="Photo of a large white luxury dream home"/>

      <polygon class="accent-stripe" points="180,290 560,244 560,258 180,304" fill="var(--slate)"/>
      <polygon class="info-band" points="0,336 180,304 560,258 560,374 0,374" fill="var(--maroon)"/>

      <g class="brand">
        <circle class="brand-dot" cx="38" cy="283" r="8" fill="var(--maroon-dark)"/>
        <text class="brand-name" x="54" y="280">Cozy Nest</text>
        <text class="brand-name" x="54" y="297">to Grand Estate</text>
      </g>

      <g class="contact">
        <circle cx="266" cy="313" r="7" fill="none" stroke="var(--ink-light)" stroke-width="1.4"/>
        <ellipse cx="266" cy="313" rx="3" ry="7" fill="none" stroke="var(--ink-light)" stroke-width="1"/>
        <line x1="259" y1="313" x2="273" y2="313" stroke="var(--ink-light)" stroke-width="1"/>
        <text class="contact-text" x="280" y="319">(555) 210-4830</text>

        <circle cx="266" cy="339" r="7" fill="var(--ink-light)"/>
        <path d="M263 335 q-1 4 3 7 q1 1 3 0 l-1 -2 q-1 1 -2 0 q-2 -2 -1 -3 l-1 -2 z" fill="var(--maroon)"/>
        <text class="contact-text" x="280" y="345">www.cozynestestate.com</text>
      </g>
    </svg>
  </div>
</body>
</html>
```